Corwin Bale Electrical would like a flyer to advertise to businesses with our services listed. our website is corwinbaleelectrical-example.com

Target Market(s)

Businesses and homes

Industry/Entity Type

Electrical

```html
<!DOCTYPE html>
<html lang="en">
<head>
<meta charset="utf-8">
<title>Corwin Bale Electrical – Flyer</title>
<link rel="stylesheet" href="https://fonts.googleapis.com/css2?family=Noto+Serif:wght@400;700&family=Lato:wght@400&display=swap">
<style>
  :root {
    --page: #e8e5e1;
    --charcoal: #2a2a2c;
    --sky: #1fb3e6;
    --sky-deep: #1496cc;
    --lime: #9ccb2c;
    --lime-light: #c3e04a;
    --lime-deep: #82b522;
    --ink: #3a3a3a;
    --white: #ffffff;
    --contact: #c6e046;
    --brand: #3fb6e8;
  }
  * { margin: 0; padding: 0; box-sizing: border-box; }
  html, body { width: 877px; height: 1200px; overflow: hidden; background: var(--page); }
  .canvas { position: relative; width: 877px; height: 1200px; }
  .shapes { position: absolute; inset: 0; }
  .brand {
    position: absolute; left: 66px; top: 316px;
    display: flex; align-items: center; gap: 10px;
    font-family: "Lato", sans-serif; font-weight: 400;
    font-size: 19px; line-height: 26px; color: var(--brand); white-space: nowrap;
  }
  .brand-mark { width: 22px; height: 22px; background: var(--lime); flex: none; }
  .about { position: absolute; left: 64px; top: 498px; width: 324px; color: var(--white); }
  .about h2 { font-family: "Noto Serif", serif; font-weight: 700; font-size: 58px; line-height: 68px; margin-bottom: 2px; }
  .about p { font-family: "Noto Serif", serif; font-size: 19.5px; line-height: 26.6px; color: #1f2a30; }
  .services-title {
    position: absolute; left: 415px; top: 603px; width: 400px; height: 82px;
    display: flex; align-items: center; justify-content: center;
    font-family: "Noto Serif", serif; font-weight: 700; font-size: 72px; color: var(--ink);
  }
  .services-list { position: absolute; left: 462px; top: 698px; width: 340px; list-style: none; }
  .services-list li {
    position: relative; padding-left: 28px; margin-bottom: 6px;
    font-family: "Noto Serif", serif; font-size: 22px; line-height: 27px; color: #1c2410;
  }
  .services-list li::before {
    content: ""; position: absolute; left: 2px; top: 9px; width: 11px; height: 11px;
    border-radius: 50%; background: var(--white);
  }
  .contacts { position: absolute; left: 66px; top: 1022px; list-style: none; }
  .contacts li {
    display: flex; align-items: center; gap: 20px; height: 34px;
    font-family: "Lato", sans-serif; font-size: 23.5px; color: var(--contact);
  }
  .contacts svg { width: 22px; height: 22px; flex: none; }
</style>
</head>
<body>
<div class="canvas">
  <svg class="shapes" width="877" height="1200" viewBox="0 0 877 1200">
    <defs>
      <linearGradient id="cityGlow" x1="0" y1="0" x2="0" y2="1">
        <stop offset="0" stop-color="#3f74c8"/>
        <stop offset="0.45" stop-color="#8a6a3c"/>
        <stop offset="1" stop-color="#c89045"/>
      </linearGradient>
      <linearGradient id="limePanel" x1="0" y1="0" x2="1" y2="0">
        <stop offset="0" stop-color="#8ec226"/>
        <stop offset="0.5" stop-color="#c3e04a"/>
        <stop offset="1" stop-color="#8ec226"/>
      </linearGradient>
      <linearGradient id="banner" x1="0" y1="0" x2="0" y2="1">
        <stop offset="0" stop-color="#ffffff"/>
        <stop offset="1" stop-color="#c9c9c9"/>
      </linearGradient>
    </defs>
    <rect class="flyer" x="36" y="55" width="804" height="1085" fill="var(--charcoal)"/>
    <path class="photo" role="img" aria-label="Photo of a lit heritage building and office tower at dusk"
          d="M335,55 L840,55 L840,620 L480,620 C380,540 318,420 312,290 C308,190 322,110 345,55 Z"
          fill="url(#cityGlow)"/>
    <path class="photo-rim" d="M345,55 C322,110 308,190 312,290 C318,420 380,540 480,600"
          fill="none" stroke="var(--lime)" stroke-width="7"/>
    <path class="green-sweep" d="M36,485 C150,425 330,415 445,478 C570,548 710,585 840,580 L840,1012 L36,1012 Z" fill="var(--lime)"/>
    <path class="blue-band" d="M36,500 C150,445 320,440 430,500 C560,568 700,600 840,598 L840,1045 L612,1102 L430,1045 L430,1012 L36,1012 Z" fill="var(--sky)"/>
    <rect class="blue-strip" x="800" y="598" width="40" height="440" fill="var(--sky-deep)"/>
    <path class="services-panel" d="M430,500 C560,566 700,596 800,594 L800,1030 L612,1087 L430,1030 Z" fill="url(#limePanel)"/>
    <rect class="services-banner" x="415" y="603" width="400" height="82" fill="url(#banner)"/>
  </svg>

  <div class="brand"><span class="brand-mark"></span>Corwin Bale Electrical</div>

  <section class="about">
    <h2>About Us</h2>
    <p>Corwin Bale Electrical Pty Ltd has over 51 years combined experience in all aspects of the electrical industry. We are committed to being on time and providing exceptional service at all times. We use an automated job tracking system from start to finish on all projects from changing a switch to large projects we have you covered with the latest in service software to ensure all works are streamlined. There is no stress of using contractors when you have us with you.</p>
  </section>

  <h2 class="services-title">Services</h2>
  <ul class="services-list">
    <li>Switchboards and Mains Upgrades</li>
    <li>Commercial and Domestic</li>
    <li>Service and construction</li>
    <li>Scheduled maintenance</li>
    <li>Lighting Installations</li>
    <li>Power Outlets</li>
    <li>Lighting Automation, installation and Led lighting</li>
    <li>24/7 Emergency Service</li>
  </ul>

  <ul class="contacts">
    <li>
      <svg viewBox="0 0 24 24" aria-hidden="true"><path fill="#fff" d="M6.6 10.8a15 15 0 0 0 6.6 6.6l2.2-2.2a1 1 0 0 1 1-.25 11.4 11.4 0 0 0 3.6.6 1 1 0 0 1 1 1V20a1 1 0 0 1-1 1A17 17 0 0 1 3 4a1 1 0 0 1 1-1h3.5a1 1 0 0 1 1 1c0 1.25.2 2.45.6 3.6a1 1 0 0 1-.25 1z"/></svg>
      0400 555 017
    </li>
    <li>
      <svg viewBox="0 0 24 24" aria-hidden="true"><rect x="3" y="6" width="18" height="13" fill="#fff"/><path d="M3 6l9 7 9-7" fill="none" stroke="#2a2a2c" stroke-width="1.6"/></svg>
      corwin@cbe-example.com.au
    </li>
    <li>
      <svg viewBox="0 0 24 24" aria-hidden="true"><circle cx="12" cy="12" r="9" fill="#fff"/><path d="M3 12h18M12 3c-3 3-3 15 0 18M12 3c3 3 3 15 0 18" fill="none" stroke="#2a2a2c" stroke-width="1.2"/></svg>
      www.corwinbaleelectrical-example.com
    </li>
  </ul>
</div>
</body>
</html>
```